Brochure Design Project

We need a brochure design for an existing small Architectural Design company. The brochure needs to be in 2 pages in A4 format to be emailed to clients as a PDF. We have written the copy for the brochure, but we are very open to any suggestions you may have here. Our logo has been designed and is attached. This design will also need to be developed into a double sided "tri-fold" A4 brochure which will printed and distributed to perspective clients. We would like portrait pictures for the key staff next to each description, but do not have these as yet. Use any photos contained on our website www.plankstudio.net.nz which you think will enhance the brochure. The brochure should reflect out website design and style.
Updates

Have changed the text file. Make sure the text file is called "profile tolland partners July 11".

Industry/Entity Type

It Company

Requirements
Must have
• Please use all the copy and logos provided. Design of brochure should fit with our existing logo. Must have a modern look with a high emphasis on design.
Nice to have
• As many photos as possible, without cluttering.
Should not have
• Must have a modern look with a high emphasis on design.

```html
<!DOCTYPE html>
<html lang="en">
<head>
<meta charset="utf-8">
<title>Tolland Partners — Architectural Design</title>
<link rel="stylesheet" href="https://fonts.googleapis.com/css2?family=Source+Sans+3:wght@400;600;700&display=swap">
<style>
  :root {
    --green: #8dc63f;
    --grey: #6d6e71;
    --black: #111111;
    --white: #ffffff;
    --photo-sky: #9fb6cc;
    --photo-wall: #d9d6cf;
    --photo-lawn: #7c9a5a;
  }
  html, body { margin: 0; padding: 0; overflow: hidden; background: var(--white); }
  .brochure {
    position: relative; width: 1200px; height: 848px; overflow: hidden;
    background: var(--white);
    font-family: "Source Sans 3", "Myriad Pro", Arial, sans-serif;
    color: var(--white);
  }
  .block { position: absolute; }
  .green { background: var(--green); }
  .grey { background: var(--grey); }
  .photo { position: absolute; }
  .photo-street { background: linear-gradient(180deg, var(--photo-sky) 0%, #c9d3dc 45%, var(--photo-wall) 70%, #8c8f91 100%); }
  .photo-lawn { background: linear-gradient(180deg, #c6d4e0 0%, var(--photo-wall) 45%, var(--photo-lawn) 75%, #5d7a4a 100%); }
  .photo-units { background: linear-gradient(180deg, #c2ccd4 0%, #e6e4df 50%, #a7a9a4 100%); }
  .photo-corner { background: linear-gradient(160deg, #a86b3a 0%, #d7d2c8 40%, #ecebe7 70%, #9a9c98 100%); }

  .brand {
    position: absolute; left: 81px; top: 75px; width: 256px; height: 100px;
    background: var(--black); display: flex; align-items: center; gap: 10px;
    padding-left: 22px; box-sizing: border-box;
  }
  .brand-mark { width: 10px; height: 10px; background: var(--green); }
  .brand-name { font-size: 30px; font-weight: 400; color: var(--white); letter-spacing: 0.5px; }

  .copy { position: absolute; font-size: 12.6px; line-height: 17.4px; margin: 0; }
  .label { position: absolute; font-size: 12px; font-weight: 600; line-height: 16px; text-transform: uppercase; margin: 0; }
  .side-label { position: absolute; left: 0; width: 102px; text-align: center; font-size: 12px; font-weight: 600; line-height: 16px; margin: 0; }

  .contact-label { position: absolute; left: 810px; top: 356px; width: 78px; text-align: right; font-size: 11px; font-weight: 600; }
  .contact { position: absolute; left: 900px; top: 372px; font-size: 11.4px; font-weight: 600; line-height: 20.5px; border-collapse: collapse; }
  .contact td { padding: 0; vertical-align: top; }
  .contact td:first-child { width: 60px; }
  .contact a { color: var(--white); }
</style>
</head>
<body>
<main class="brochure">
  <!-- grid blocks -->
  <div class="block grey" style="left:0;top:0;width:102px;height:129px"></div>
  <div class="block green" style="left:104px;top:0;width:414px;height:129px"></div>
  <div class="block green" style="left:0;top:131px;width:102px;height:576px"></div>
  <div class="block green" style="left:0;top:709px;width:102px;height:139px"></div>
  <div class="block grey" style="left:104px;top:131px;width:404px;height:434px"></div>
  <div class="block grey" style="left:403px;top:567px;width:105px;height:281px"></div>
  <div class="block green" style="left:510px;top:131px;width:328px;height:717px"></div>
  <div class="block grey" style="left:840px;top:131px;width:52px;height:211px"></div>
  <div class="block grey" style="left:840px;top:344px;width:360px;height:209px"></div>

  <!-- photography areas -->
  <div class="photo photo-street" style="left:520px;top:0;width:680px;height:129px" role="img" aria-label="Photo of a multi-unit residential development along a street"></div>
  <div class="photo photo-lawn" style="left:894px;top:131px;width:306px;height:211px" role="img" aria-label="Photo of apartment buildings beside a bowling green"></div>
  <div class="photo photo-units" style="left:104px;top:567px;width:297px;height:281px" role="img" aria-label="Photo of white two-storey townhouses"></div>
  <div class="photo photo-corner" style="left:840px;top:555px;width:360px;height:293px" role="img" aria-label="Photo of a modern apartment block on a street corner with autumn trees"></div>

  <div class="brand">
    <span class="brand-mark"></span>
    <span class="brand-name">tolland partners</span>
  </div>

  <p class="side-label" style="top:407px">CLIENT<br>FOCUSED:</p>

  <p class="copy" style="left:124px;top:178px;width:292px">Tolland Partners Limited is an Architectural Design practise based in Hamilton and provides Architectural and Development consultation services in the Waikato, Coromandel, Auckland and Bay of Plenty regions and is recognised for providing innovative design solutions to many satisfied clients. The architectural character of each building we design is unique because every design is a response to several factors including climate, views, topography, site context, functional program and the aesthetic sensibilities of our clients, infused with our own architectural vision.</p>
  <p class="copy" style="left:124px;top:404px;width:292px">Right from the early stages of the design process the Client is an integral part of the team. By listening to our clients we are able to deliver design solutions which meet their individual requirements and allows us to draw on our years of experience to create designs which are exciting, distinctive and cost effective.</p>

  <p class="label" style="left:433px;top:172px">Project<br>Experience:</p>
  <p class="label" style="left:433px;top:222px">Residential:</p>
  <p class="label" style="left:433px;top:377px">Remedial:</p>
  <p class="label" style="left:433px;top:515px">Multi-Unit<br>Residential:</p>
  <p class="label" style="left:433px;top:686px">Commercial:</p>

  <p class="copy" style="left:518px;top:240px;width:314px">Residential projects require a unique blend of creativity and client consideration. We have a vast range of experience in designing and documenting new homes, house relocations and house alterations for many satisfied clients, from simple 2 bedroom units to large multi level dwellings.</p>
  <p class="copy" style="left:518px;top:395px;width:314px">Remedial work is an increasing body of work as a result of New Zealand's leaky building crisis and is fast becoming a large part of the New Zealand Building Industry landscape. We have the experience and contacts to work in with and if necessary lead the remediation team.</p>
  <p class="copy" style="left:518px;top:553px;width:314px">Having successfully completed the design and documentation for over 150 Multi-Unit residential developments, we have demonstrated that we are well resourced to offer a range of skills for any development of this nature. With two national design awards for this type of design, we can rightly claim to be experts in this field.</p>
  <p class="copy" style="left:518px;top:717px;width:314px">Good design adds value to any project, especially Commercial projects. As the design team leader, Tolland Partners has a track record of leading exciting and dynamic commercial developments.</p>

  <div class="contact-label">Contact :</div>
  <table class="contact">
    <tr><td colspan="2">PO Box 40512</td></tr>
    <tr><td colspan="2">Hamilton 3250</td></tr>
    <tr><td colspan="2">New Zealand</td></tr>
    <tr><td>Ph</td><td>64 7 8401236</td></tr>
    <tr><td>Fax</td><td>64 7 8401237</td></tr>
    <tr><td>Mob</td><td>021558310</td></tr>
    <tr><td>email:</td><td><a href="mailto:admin@plankstudio.net.nz">admin@plankstudio.net.nz</a></td></tr>
    <tr><td>Website:</td><td><a href="http://www.plankstudio.net.nz">www.plankstudio.net.nz</a></td></tr>
  </table>
</main>
</body>
</html>
```